Firma sucht ansprechendes Einfahrtsschild
Zielgruppe
Firmen, sowie Privatpersonen / Laufkundschaft
Aufgabenstellung
Wir suchen für unser Hof ein neues Einfahrtsschild wie z.B. unser selbstversuch Hofschild 3.6.2015 // es hat auch jemand man etwas für uns gemacht vor langer zeit was aber nie benutzt wurde siehe M1 ///
wir suchen mehr etwas was den Leuten auffällt und das wesentliche rüber bringt.

```html
<!DOCTYPE html>
<html lang="de">
<head>
<meta charset="utf-8">
<title>Einfahrtsschild Wäscherei Kleeberg</title>
<link rel="stylesheet" href="https://fonts.googleapis.com/css2?family=Arimo:wght@400;700&display=swap">
<style>
  :root {
    --page-bg: #e6e6e6;
    --sign-white: #ffffff;
    --brand-blue: #2f3585;
    --parking-blue: #2f3585;
    --arrow-red: #d6202c;
    --arrow-red-light: #e8404a;
    --band-green: #77b544;
    --scene-grey-1: #e2e2e2;
    --scene-grey-2: #c9c9c9;
    --text-grey: #555555;
  }
  * { box-sizing: border-box; margin: 0; padding: 0; }
  html, body {
    width: 1200px; height: 1062px; overflow: hidden;
    background: var(--page-bg);
    font-family: "Arimo", Arial, sans-serif;
  }
  .sign {
    position: absolute; left: 40px; top: 136px;
    width: 1120px; height: 790px;
    background: var(--sign-white);
    box-shadow: 0 6px 18px rgba(0,0,0,.18);
    overflow: hidden;
  }
  .sign-header {
    position: absolute; left: 0; top: 0; width: 100%; height: 155px;
    background: var(--sign-white);
  }
  .brand {
    position: absolute; left: 34px; top: 30px;
    display: flex; align-items: center; gap: 22px;
  }
  .brand-mark {
    width: 100px; height: 100px; border-radius: 50%;
    background: var(--band-green);
  }
  .brand-name {
    font-size: 54px; font-weight: 700; color: var(--brand-blue);
    line-height: 1;
  }
  .brand-tagline {
    margin-top: 10px; font-size: 17px; color: var(--text-grey);
  }
  .parking {
    position: absolute; left: 752px; top: 24px;
    display: flex; align-items: center; gap: 18px;
  }
  .parking-icon { width: 113px; height: 113px; }
  .parking-text {
    font-size: 42px; font-weight: 700; color: var(--parking-blue);
    line-height: 1.1;
  }
  .scene {
    position: absolute; left: 0; top: 155px; width: 100%; height: 546px;
    background: linear-gradient(180deg, var(--scene-grey-1), var(--scene-grey-2));
  }
  .direction-arrow {
    position: absolute; left: 31px; top: 327px;
    width: 660px; height: 256px;
  }
  .direction-label {
    position: absolute; left: 225px; top: 412px;
    width: 440px; text-align: center;
    font-size: 78px; font-weight: 700; color: #fff; line-height: 1;
  }
  .footer-band {
    position: absolute; left: 0; bottom: 0; width: 100%; height: 89px;
    background: var(--band-green);
    display: flex; align-items: center; justify-content: center;
    font-size: 50px; font-weight: 700; color: #fff; letter-spacing: 1px;
  }
</style>
</head>
<body>
  <div class="sign">
    <header class="sign-header">
      <div class="brand">
        <div class="brand-mark"></div>
        <div>
          <div class="brand-name">Wäscherei Kleeberg</div>
          <div class="brand-tagline">Sauberkeit und Frische aus dem Meisterbetrieb</div>
        </div>
      </div>
      <div class="parking">
        <svg class="parking-icon" viewBox="0 0 113 113" aria-hidden="true">
          <rect x="0" y="0" width="113" height="113" rx="12" fill="var(--parking-blue)"/>
          <rect x="7" y="7" width="99" height="99" rx="8" fill="none" stroke="#fff" stroke-width="4"/>
          <text x="56.5" y="88" text-anchor="middle" font-family="Arimo, Arial, sans-serif" font-weight="700" font-size="84" fill="#fff">P</text>
        </svg>
        <div class="parking-text">Parkplätze<br>im HOF!</div>
      </div>
    </header>

    <div class="scene" role="img" aria-label="Illustration: Waschsalon mit Waschmaschinen und einer Frau mit vollem Wäschekorb"></div>

    <svg class="direction-arrow" viewBox="0 0 660 256" aria-hidden="true">
      <polygon points="0,128 166,0 166,56 656,56 656,200 166,200 166,256" fill="var(--arrow-red)" stroke="#fff" stroke-width="6" stroke-linejoin="round"/>
      <polygon points="12,128 160,14 160,62 650,62 650,110 12,128" fill="var(--arrow-red-light)" opacity=".45"/>
    </svg>
    <div class="direction-label">Wäscherei</div>

    <footer class="footer-band">AUCH FÜR PRIVAT</footer>
  </div>
</body>
</html>
```